8-seitig Analyse: aufräumen/Kernaussagen optimieren
Zielgruppe
Meine Firma wendet sich an HR-Verantwortliche und unterstütze sie speziell im Bereich Recruiting.
Aufgabenstellung
Ich habe eine 8-seitige (mit Deckblatt und Kontaktseite) Analyse entwickelt. Diese 'Insights' sind auch bereits fertig 'designt'. Allerdings müssen manche Analyse-Ergebnisse optisch noch optimiert werden, Die Seiten eventuell etwas aufgeräumt und vor allem die Kernaussage eines Ergebnisses in 'optisches Drama' übersetzt werden.
Ziel:
Jemand der die Analyse nur schnell überfliegen möchte, soll die wichtigsten Infos auch beim schnellen 'Überblättern' erfassen können. Er soll die ganze Dramtik erfassen können und erkennen, dass ihm geholfen werden kann.
Konkret:
Auf den Seiten 2-7 werden mit Text und Diagrammen/Tabelle bestimmte Aussagen nachweisbar hergeleitet. Die jeweilige Kernaussage soll nun noch optisch präsenter werden. Es braucht manchmal mehr 'Drama', mehr 'Schmerz'...
Eventuell müssen die Seiten für das Auge etwas besser strukturiert werden - im Sinne von : Aufgeräumt, gefälliger fürs Auge
Außerdem:
Die Hintergrundgrafik der Seiten (lila schräge) und der Hintergrund der letzte Seite ist als 16:9 konzipiert worden und musste für DIN A4 neu skaliert werden. Da ich kein Profi bin, ist dieser nun pixelig geworden. Wäre schön, wenn ihr mir diesen wieder schärfen könntet.
Und wenn Du eine Idee hast, wie man die Ausagen durch vielleicht besser Darstellungen/Diagramme/Tabelle darstellen könnte, immer gerne.
Ich hänge gleich die konkreten Anmerkungen für die jeweiligen Seite an das Projekt, damit ihr den Umfang richtgi abschätzen könnt.
Ich freue mich schon auf eure Idee. Ansonsten einfach Fragen, wenn etwas nicht verständlich ist.
LG
qLumrit
Nachtrag: 09.02.21 - 17:15 Uhr:
Ich habe die PPT-Datei als Arbeitsdatei hochgeladen, so dass man die ganze Analyse nicht erst nachbauen muss. Im Ergebnis benötige ich aber keine PPT-Datei.
Mir reicht das PSD oder eben auch das PDF, dass ich dann hier lokal in mein..

```html
<!DOCTYPE html>
<html lang="de">
<head>
<meta charset="utf-8">
<title>Insights – Einblick Arbeitsmarkt / Regionale Zielmärkte</title>
<link rel="stylesheet" href="https://fonts.googleapis.com/css2?family=Ubuntu:wght@400;500;700&display=swap">
<style>
  :root {
    --stage: #dcdcde;
    --paper: #f4f4f6;
    --ink: #231c4d;
    --ink-soft: #4a4660;
    --violet-deep: #1f1a45;
    --violet: #4b1c63;
    --violet-bright: #6a2379;
    --lavender: #8c5a9e;
    --gold: #e7b94a;
    --gold-dark: #c99a2a;
    --map-blue: #3a9bd0;
    --map-violet: #703684;
    --white: #ffffff;
  }
  * { box-sizing: border-box; margin: 0; padding: 0; }
  html, body { width: 1200px; height: 1011px; overflow: hidden; }
  body {
    background: var(--stage);
    font-family: "Ubuntu", sans-serif;
    color: var(--ink);
  }
  .spread {
    position: absolute;
    left: 25px; top: 170px;
    width: 1150px; height: 670px;
    display: flex;
    box-shadow: 0 18px 40px rgba(0,0,0,.18);
  }
  .page {
    position: relative;
    width: 575px; height: 670px;
    background: var(--paper);
    overflow: hidden;
  }
  .page-bg { position: absolute; inset: 0; width: 100%; height: 100%; }
  .brand {
    position: absolute; top: 18px; right: 24px;
    font-size: 9px; font-weight: 500; color: var(--violet-bright);
  }
  .intro { position: absolute; left: 40px; top: 70px; width: 500px; }
  .intro h1 { font-size: 24px; font-weight: 700; color: var(--ink); margin-bottom: 12px; }
  .intro p { font-size: 11px; line-height: 1.45; color: var(--ink-soft); margin-bottom: 10px; }
  .on-dark { color: var(--white); }
  .section-title { font-size: 20px; font-weight: 500; line-height: 1.2; }
  .caption { font-size: 9px; line-height: 1.3; opacity: .85; white-space: nowrap; }

  .vakanz { position: absolute; left: 40px; top: 372px; }
  .stat { position: absolute; display: flex; align-items: center; gap: 12px; }
  .stat-ring { position: relative; width: 84px; height: 84px; flex: none; }
  .stat-ring svg { width: 84px; height: 84px; }
  .ring-label {
    position: absolute; inset: 0; display: flex; align-items: center; justify-content: center;
    text-align: center; font-size: 14px; line-height: 1.1; color: var(--white);
  }
  .connector { width: 30px; height: 2px; background: var(--gold); flex: none; }
  .stat-text { font-size: 13px; line-height: 1.2; color: var(--white); white-space: nowrap; }
  .stat-text small { display: block; font-size: 9px; opacity: .85; margin-top: 2px; }
  .stat-value { font-size: 15px; color: var(--white); white-space: nowrap; }
  .stat-duration { left: 40px; top: 414px; }
  .stat-open { left: 230px; top: 478px; }

  .cost { position: absolute; left: 60px; top: 568px; color: var(--white); }
  .cost h3 { font-size: 16px; font-weight: 500; line-height: 1.2; white-space: nowrap; }
  .cost .caption { margin-bottom: 3px; }
  .cost .line { font-size: 10px; font-weight: 500; line-height: 1.15; white-space: nowrap; }
  .cost .figure { font-size: 17px; font-weight: 700; color: var(--gold); }
  .cost .line-2 { padding-left: 40px; }
  .cost .line-3 { padding-left: 80px; }

  .market { position: absolute; left: 40px; top: 470px; width: 250px; }
  .market h2 { font-size: 22px; font-weight: 500; line-height: 1.3; margin-bottom: 14px; }
  .market p { font-size: 12px; line-height: 1.4; }
  .map-area {
    position: absolute; left: 320px; top: 325px; width: 220px; height: 290px;
    background: linear-gradient(160deg, var(--map-blue) 0%, var(--map-blue) 40%, var(--map-violet) 55%, var(--map-violet) 100%);
    border-radius: 40% 30% 35% 30% / 20% 25% 30% 35%;
    opacity: .9;
  }
  .map-source { position: absolute; right: 18px; top: 620px; font-size: 6px; color: var(--white); opacity: .6; }
</style>
</head>
<body>
  <main class="spread">
    <section class="page page-left">
      <svg class="page-bg" viewBox="0 0 575 670" preserveAspectRatio="none" aria-hidden="true">
        <defs>
          <linearGradient id="leftBand" x1="0" y1="0" x2="1" y2="1">
            <stop offset="0" stop-color="#1f1a45"/>
            <stop offset=".55" stop-color="#4b1c63"/>
            <stop offset="1" stop-color="#6b5a8e"/>
          </linearGradient>
          <linearGradient id="leftLow" x1="0" y1="1" x2="1" y2="0">
            <stop offset="0" stop-color="#4e1a5e"/>
            <stop offset=".5" stop-color="#3a2a62"/>
            <stop offset="1" stop-color="#666082"/>
          </linearGradient>
          <linearGradient id="leftWedge" x1="0" y1="0" x2="1" y2="0">
            <stop offset="0" stop-color="#2c1f55"/>
            <stop offset="1" stop-color="#8c5a9e"/>
          </linearGradient>
        </defs>
        <path d="M300 300 Q430 250 575 200 L575 320 Q460 330 300 300 Z" fill="url(#leftWedge)"/>
        <path d="M0 330 Q300 330 575 395 L575 670 L0 670 Z" fill="url(#leftBand)"/>
        <path d="M300 300 Q460 335 575 395 L575 402 Q450 345 300 300 Z" fill="#f4f4f6"/>
        <path d="M0 372 Q300 360 575 420 L575 670 L0 670 Z" fill="url(#leftLow)"/>
      </svg>
      <div class="brand">Corvana Consulting</div>
      <div class="intro">
        <h1>Einblick Arbeitsmarkt</h1>
        <p>Diese zwei Indikatoren geben uns eine realistische Einschätzung darüber, wie schwer, wie umkämpft und letztlich auch, wie teuer es werden wird, die offene Stelle im Bereich Elektrotechnik zu besetzen.</p>
        <p>Allein eine einzige offene Stelle im Bereich Elektrotechnik, die erst nach 165 Tagen besetzt wird, kostet ein Unternehmen etwa 87.517 EUR in Produktivitätsausfall</p>
      </div>

      <div class="vakanz on-dark">
        <h2 class="section-title">Der Vakanztest</h2>
        <p class="caption">ohne Zeitarbeitsunternehmen; Datenbestand Januar 2021</p>
      </div>

      <div class="stat stat-duration">
        <div class="stat-ring">
          <svg viewBox="0 0 96 96" aria-hidden="true">
            <circle cx="48" cy="48" r="38" fill="none" stroke="#5a2a72" stroke-width="12"/>
            <circle cx="48" cy="48" r="38" fill="none" stroke="var(--gold-dark)" stroke-width="12"
                    stroke-dasharray="180 239" transform="rotate(-90 48 48)"/>
          </svg>
          <div class="ring-label">165<br>Tage</div>
        </div>
        <div class="connector"></div>
        <div class="stat-text">durchschnittliche<br>Besetzungsdauer<small>alle Berufsgruppen: 134 Tage</small></div>
      </div>

      <div class="stat stat-open">
        <div class="stat-text">nach drei Monaten<br>immer noch unbesetzt<small>alle Berufsgruppen: 51,8%</small></div>
        <div class="connector"></div>
        <div class="stat-value">56,4%</div>
        <div class="stat-ring">
          <svg viewBox="0 0 96 96" aria-hidden="true">
            <circle cx="48" cy="48" r="38" fill="none" stroke="#7a3c8e" stroke-width="14"
                    stroke-dasharray="135 239" transform="rotate(-90 48 48)"/>
            <circle cx="48" cy="48" r="36" fill="none" stroke="var(--gold)" stroke-width="10"
                    stroke-dasharray="127 226" transform="rotate(-90 48 48)"/>
          </svg>
        </div>
      </div>

      <div class="cost">
        <h3>Kosten des Produktivitätsausfalls</h3>
        <p class="caption">Berechnung costs of low productivity nach Weston Business School</p>
        <p class="line"><span class="figure">87.517</span> EUR oder</p>
        <p class="line line-2">jeden Tag <span class="figure">530</span> EUR</p>
        <p class="line line-3">solange die Stelle nicht besetzt ist</p>
      </div>
    </section>

    <section class="page page-right">
      <svg class="page-bg" viewBox="0 0 575 670" preserveAspectRatio="none" aria-hidden="true">
        <defs>
          <linearGradient id="rightBand" x1="0" y1="1" x2="1" y2="0">
            <stop offset="0" stop-color="#1f1a45"/>
            <stop offset=".5" stop-color="#2a1d52"/>
            <stop offset="1" stop-color="#6a2379"/>
          </linearGradient>
          <linearGradient id="rightWedge" x1="0" y1="0" x2="1" y2="0">
            <stop offset="0" stop-color="#4b1c63"/>
            <stop offset="1" stop-color="#1f1a45"/>
          </linearGradient>
        </defs>
        <path d="M0 260 L360 300 L575 200 L575 670 L0 670 Z" fill="url(#rightWedge)"/>
        <path d="M0 420 Q250 380 575 230 L575 670 L0 670 Z" fill="url(#rightBand)"/>
        <path d="M0 395 L360 300 L0 390 Z" fill="#f4f4f6"/>
      </svg>
      <div class="brand">Corvana Consulting</div>
      <div class="intro">
        <h1>Regionale Zielmärkte</h1>
        <p>Moderne, digitale Rekrutierungsstrategien steigern die Besetzungschancen, indem offene Vakanzen auch außerhalb des regionalen Marktes beworben werden.</p>
        <p>In welchen Regionen es sich für uns lohnt, gezielt neue, zusätzliche Zielgruppen der Berufskategorie Elektrotechnik zu bewerben, zeigt nebenstehende Karte.</p>
      </div>

      <div class="market on-dark">
        <h2>Marktumfeld und<br>Engpassanalyse</h2>
        <p>Auf je 100 offene Stellen<br>im Bereich Elektrotechnik<br>kommen … arbeitsuchende<br>Elektrotechniker</p>
      </div>

      <div class="map-area" role="img" aria-label="Deutschlandkarte nach Bundesländern: Norden und Westen blau hervorgehoben, übrige Länder violett, mit Kennzahlen je Region zwischen 101 und 196"></div>
      <p class="map-source">Quelle: Regionaldaten 2021</p>
    </section>
  </main>
</body>
</html>
```